BrindleQuartos

We need a book cover for an upcoming book publication. Please see attachment for the text that should go on the book cover. We want a sleek and impacting design, but not overly busy. The target industry is oral-maxillofacial. Thanks and good luck!

```html
<!DOCTYPE html>
<html lang="en">
<head>
<meta charset="utf-8">
<title>BrindleQuartos – Book Cover</title>
<link rel="stylesheet" href="https://fonts.googleapis.com/css2?family=Arimo:wght@400;700&display=swap">
<style>
  :root {
    --page-bg: #e9ecee;
    --cover-top: #a9e0e7;
    --cover-bottom: #86d1dc;
    --cream: #f3f6d8;
    --teal: #2b8c98;
    --teal-deep: #1d6a78;
    --orange: #e27a1e;
    --ink: #27434a;
    --rule: #1e5563;
  }
  * { box-sizing: border-box; margin: 0; padding: 0; }
  html, body {
    width: 1200px;
    height: 783px;
    overflow: hidden;
    background: var(--page-bg);
    font-family: "Arimo", Arial, sans-serif;
  }
  .book {
    position: absolute;
    top: 40px;
    left: 325px;
    display: flex;
    height: 703px;
    box-shadow: 0 10px 30px rgba(0,0,0,0.18);
  }
  .spine {
    position: relative;
    width: 62px;
    height: 100%;
    background: var(--cream);
    border-right: 1px solid rgba(0,0,0,0.08);
  }
  .spine-line {
    position: absolute;
    left: 29px;
    width: 2px;
    background: var(--teal);
  }
  .spine-line.top { top: 30px; height: 70px; }
  .spine-line.bottom { bottom: 30px; height: 70px; }
  .spine-title {
    position: absolute;
    top: 50%;
    left: 50%;
    transform: translate(-50%, -50%) rotate(90deg);
    white-space: nowrap;
    color: var(--teal);
    font-size: 38px;
    letter-spacing: 1px;
  }
  .cover {
    position: relative;
    width: 490px;
    height: 100%;
    background: linear-gradient(180deg, var(--cover-top), var(--cover-bottom));
    overflow: hidden;
  }
  .profile-art {
    position: absolute;
    left: 0;
    top: 0;
    width: 118px;
    height: 100%;
  }
  .author {
    position: absolute;
    top: 34px;
    left: 130px;
    color: var(--teal);
    font-size: 15px;
  }
  .title {
    position: absolute;
    top: 108px;
    left: 122px;
    color: var(--teal-deep);
    font-size: 44px;
    font-weight: 400;
    letter-spacing: -0.5px;
  }
  .pronunciation {
    position: absolute;
    top: 164px;
    left: 124px;
    color: var(--orange);
    font-size: 17px;
    white-space: nowrap;
  }
  .title-rule {
    position: absolute;
    top: 206px;
    left: 268px;
    width: 110px;
    height: 2px;
    background: var(--rule);
  }
  .definitions {
    position: absolute;
    top: 232px;
    left: 130px;
    width: 330px;
    list-style: none;
    color: var(--ink);
    font-size: 10.5px;
    line-height: 1.35;
  }
  .definitions li { display: flex; gap: 10px; margin-bottom: 22px; }
  .definitions li:nth-child(2) { padding-left: 18px; }
  .definitions li:nth-child(3) { padding-left: 30px; }
  .definitions .num { flex: none; }
  .quote {
    position: absolute;
    bottom: 30px;
    right: 40px;
    color: var(--orange);
    font-size: 14px;
  }
</style>
</head>
<body>
  <div class="book">
    <div class="spine">
      <span class="spine-line top"></span>
      <span class="spine-title">BrindleQuartos</span>
      <span class="spine-line bottom"></span>
    </div>
    <section class="cover">
      <svg class="profile-art" role="img" aria-label="Cream silhouette of a human side profile" viewBox="0 0 118 703" preserveAspectRatio="none">
        <rect width="118" height="703" fill="var(--cream)"/>
      </svg>
      <p class="author">Author or Book Publisher</p>
      <h1 class="title">BrindleQuartos</h1>
      <p class="pronunciation">noun &nbsp;| \ brin - dəl - \ kwôr - tōz</p>
      <span class="title-rule"></span>
      <ol class="definitions">
        <li><span class="num">1 &nbsp;:</span><span>the practice of clinical aesthetics with medical-grade products.</span></li>
        <li><span class="num">2 &nbsp;:</span><span>a universal clinical perception of natural geometric forms and height of contours.</span></li>
        <li><span class="num">3 &nbsp;:</span><span>aesthetic diagnosis and treatment knowledgebase.</span></li>
      </ol>
      <p class="quote">"Quote or quotes if needed"</p>
    </section>
  </div>
</body>
</html>
```